Design a flyer

Hi, I need a flyer designed for an electrical and air conditioning company based in brisbane, Australia.
We service the domestic market.
Flyer is to be double sided
Flyer size DL 210mm X 99mm
Was thinking one side services and discount coupons and the other side possible testimonials.
I have logo uploaded followed with the vehicle advertising, advertising stand alone sign and also business cards.
--------------------------
Coupon Cut out
save $150 OFF switchboard upgrades
save $150 Complimentary Electrical safety inspection
save $50 OFF Air Conditioner install or Service
save $50 next job if you leave feedback for first job
OVER $400 WORTH OF SAVINGS!
Our promise to you
* we will Arrive on time or we will pay you $100
* Before any job begins you will know the exact price
* We will leave your place as clean as we arrived
* if there is a problem and its our fault we will fix it for free
* provide a 12 month warranty on all parts
* we will provide friendly helpful service and advice
Phone number is 0487 562 903
Company Name - Quillbrook
License: 58164
ABN - 61 208 359 772
Also add swift pay, nexo and tapnet logo at the bottom
----------------------------
Here is what some of my customers have had to say
Extremely professional...
“Arrived when he said he would, sent through a written quote and was very reasonable. He also checked out our smoke
detectors whist he was here. He installed 2 ceiling fans and an air conditioner. He
cleaned up the mess and was very efficient. I will definitely use him again and recommend
him to family and friends”
P.M – Stretton
“Excellent service provider. He arrived on time with a call before arriving, than carried all jobs quickly and efficiently and left no mess at all. I will definitely recommend his service to others requiring an electrician. Thanks again!”
R.T – Greenslopes
“Over the long weekend, I had problems with my power, not only did you pick up the first phone call but you came out at 5am to fix it. Love the fact you’re a 24hr service!”
K.L – Mount Gravatt
---------------------------
NEW changes
Hi everyone,
Just want to say well done all the designers look great!
I will soon be choosing a winner, but there are a couple of changes i would like to make, if you revise you will be in for a win.
Instead of Save 50 if you leave feedback for the first job quote. I want to change that put $110 cross out and put $71.50 Install & Supply LED Downlights (min 20)
I want this to be the number one followed by switch board upgrade cut out.
Also $50 off air con install - don't put service.
And the third testimonial K.L Make sure it has a full stop
Also keep in mind. It is an electrical & air conditioning company.
Be creative with your design, don't want to see any pictures of people as they are not working for us at this time.
Remember key focus, on coupons, phone numbers, and website. nexo and swiftpay can be small and out of the way same with the license numbers.
Thank you
Good Luck!
Domestic Market - Home owners
Air Conditioning

```html
<!DOCTYPE html>
<html lang="en">
<head>
<meta charset="utf-8">
<title>Quillbrook – DL Flyer</title>
<link href="https://fonts.googleapis.com/css2?family=Questrial&family=Barlow+Condensed:ital,wght@1,400;1,600;1,700;1,800&family=Oswald:wght@500;600&display=swap" rel="stylesheet">
<style>
  :root{
    --brand-blue:#1479c4;
    --logo-blue:#1f6fb8;
    --swoosh-orange:#f05a28;
    --accent-yellow:#f7b733;
    --navy:#1d3a8a;
    --coupon-1:#ef3b36;
    --coupon-2:#f05a2a;
    --coupon-3:#f5901e;
    --coupon-4:#fbb040;
    --white:#ffffff;
    --page:#ffffff;
  }
  *{margin:0;padding:0;box-sizing:border-box}
  html,body{width:1200px;height:1200px;overflow:hidden;background:var(--page)}
  .sheet{position:relative;width:1200px;height:1200px}
  .panel{position:absolute;top:27px;width:540px;height:1146px;border:1.5px solid var(--brand-blue);overflow:hidden;background:var(--white)}
  .panel--front{left:33px}
  .panel--back{left:627px}
  .backdrop{position:absolute;left:0;top:0;width:540px;height:820px}
  .brand{position:absolute;left:0;right:0;top:72px;text-align:center;
    font-family:"Questrial",sans-serif;font-size:64px;color:var(--logo-blue);letter-spacing:2px}
  .services{position:absolute;left:20px;top:316px;width:510px;
    font-family:"Barlow Condensed",sans-serif;font-style:italic;font-weight:700;font-size:20px;line-height:27px;color:var(--accent-yellow)}
  .promise{position:absolute;left:20px;top:408px;font-family:"Barlow Condensed",sans-serif;font-style:italic;color:var(--white)}
  .promise h2{font-weight:700;font-size:23px;margin-bottom:8px}
  .promise li{list-style:none;font-weight:700;font-size:19.5px;line-height:34.8px}
  .testimonials{position:absolute;left:20px;top:316px;width:505px;font-family:"Barlow Condensed",sans-serif;font-style:italic;color:var(--white)}
  .testimonials h2{font-weight:700;font-size:16.5px;margin-bottom:18px}
  .quote{font-weight:400;font-size:16px;line-height:20.8px;margin-bottom:21px;letter-spacing:-.2px}
  .quote cite{display:block;font-style:italic;font-weight:600}
  .call{position:absolute;left:20px;top:700px;font-family:"Barlow Condensed",sans-serif;font-style:italic;font-weight:800}
  .call__label{font-size:29px;line-height:30px;color:var(--accent-yellow)}
  .call__number{font-size:44px;line-height:44px;color:var(--white)}
  .payments{position:absolute;left:272px;top:700px;width:250px;height:74px;background:var(--white);border-radius:16px;
    display:flex;align-items:center;justify-content:space-around;padding:0 10px;
    font-family:"Barlow Condensed",sans-serif;font-style:italic;font-weight:700;font-size:21px;color:var(--navy)}
  .savings{position:absolute;left:0;top:790px;width:100%;height:40px;background:var(--white);text-align:center;
    font-family:"Oswald",sans-serif;font-weight:600;font-size:29px;line-height:40px;color:var(--navy);transform-origin:center}
  .coupons{position:absolute;left:0;top:830px;width:100%}
  .coupon{height:78.8px;display:flex;align-items:center;justify-content:center;border-top:1.5px dashed var(--navy);
    font-family:"Oswald",sans-serif;font-weight:500;font-size:19px;color:var(--white)}
  .coupon--switchboard{background:var(--coupon-1)}
  .coupon--inspection{background:var(--coupon-2)}
  .coupon--aircon{background:var(--coupon-3)}
  .coupon--feedback{background:var(--coupon-4)}
</style>
</head>
<body>
<main class="sheet">

  <section class="panel panel--front">
    <svg class="backdrop" viewBox="0 0 540 820" aria-hidden="true">
      <path d="M0,178 C120,190 230,300 360,292 C440,287 500,252 540,212 L540,820 L0,820 Z" fill="var(--brand-blue)"/>
      <path d="M155,200 Q380,305 540,168 L540,198 Q390,312 155,200 Z" fill="var(--swoosh-orange)"/>
    </svg>
    <h1 class="brand">Quillbrook</h1>
    <p class="services">24 hour service • Electrical • Air Conditioning • Domestic<br>Commercial • Install • Service • Maintenance</p>
    <div class="promise">
      <h2>Our promise to YOU</h2>
      <ul>
        <li>* we will Arrive on time or we will pay you $100</li>
        <li>* Before any job begins you will know the exact price</li>
        <li>* We will leave your place as clean as we arrived</li>
        <li>* if there is a problem and its our fault we will fix it for free</li>
        <li>* provide a 12 month warranty on all parts</li>
        <li>* we will provide friendly helpful service and advice</li>
      </ul>
    </div>
    <div class="call">
      <p class="call__label">GIVE US A CALL</p>
      <p class="call__number">0487 562 903</p>
    </div>
    <div class="payments"><span>nexo</span><span>swiftpay</span><span>tapnet</span></div>
    <p class="savings">OVER $400 WORTH OF SAVINGS!</p>
    <div class="coupons">
      <div class="coupon coupon--switchboard">SAVE $150 OFF SWITCHBOARD UPGRADES</div>
      <div class="coupon coupon--inspection">SAVE $150 COMPLIMENTARY ELECTRICAL SAFETY INSPECTION</div>
      <div class="coupon coupon--aircon">SAVE $50 OFF AIR CONDITIONER INSTALL OR SERVICE</div>
      <div class="coupon coupon--feedback">SAVE $50 NEXT JOB IF YOU LEAVE FEEDBACK FOR FIRST JOB</div>
    </div>
  </section>

  <section class="panel panel--back">
    <svg class="backdrop" viewBox="0 0 540 820" aria-hidden="true">
      <path d="M0,178 C120,190 230,300 360,292 C440,287 500,252 540,212 L540,820 L0,820 Z" fill="var(--brand-blue)"/>
      <path d="M155,200 Q380,305 540,168 L540,198 Q390,312 155,200 Z" fill="var(--swoosh-orange)"/>
    </svg>
    <h1 class="brand">Quillbrook</h1>
    <div class="testimonials">
      <h2>Here is what some of my customers have had to say</h2>
      <p class="quote">Extremely professional...<br>“Arrived when he said he would, sent through a written quote and was very reasonable. He also checked out our smoke detectors whist he was here. He installed 2 ceiling fans and an air conditioner. He cleaned up the mess and was very efficient. I will definitely use him again and recommend him to family and friends”<cite>P.M – Stretton</cite></p>
      <p class="quote">“Excellent service provider. He arrived on time with a call before arriving, than carried all jobs quickly and efficiently and left no mess at all. I will definitely recommend his service to others requiring an electrician. Thanks again!”<cite>R.T – Greenslopes</cite></p>
      <p class="quote">“Over the long weekend, I had problems with my power, not only did you pick up the first phone call but you came out at 5am to fix it. Love the fact you’re a 24hr service!”<cite>K.L – Mount Gravatt</cite></p>
    </div>
    <div class="call">
      <p class="call__label">GIVE US A CALL</p>
      <p class="call__number">0487 562 903</p>
    </div>
    <div class="payments"><span>nexo</span><span>swiftpay</span><span>tapnet</span></div>
    <p class="savings">OVER $400 WORTH OF SAVINGS!</p>
    <div class="coupons">
      <div class="coupon coupon--switchboard">SAVE $150 OFF SWITCHBOARD UPGRADES</div>
      <div class="coupon coupon--inspection">SAVE $150 COMPLIMENTARY ELECTRICAL SAFETY INSPECTION</div>
      <div class="coupon coupon--aircon">SAVE $50 OFF AIR CONDITIONER INSTALL OR SERVICE</div>
      <div class="coupon coupon--feedback">SAVE $50 NEXT JOB IF YOU LEAVE FEEDBACK FOR FIRST JOB</div>
    </div>
  </section>

</main>
</body>
</html>
```